High end personal training flyer design

I want a flyer designed to be delivered to people's houses to interest them in high end (and, therefore, not cheap) personal training services.

Don't want standard pictures of people exercising, before and afters, etc. More something that will appeal to that more affluent market.

Flexible on size of flyer, but please make sure it is a standard size that I can get printed easily. Would like it not to look like a normal flyer you get through the letterbox, so if any particular sizes, shapes, etc are known to do that, then that would be a good start.

Text on flyer to be as follows:

Is this you:

Live in East Cheshire
Male, aged 30-50
A father
Cash rich, time poor
Find handling high pressure at work comfortable
But have a short fuse out of work – with the wife, kids, life in general, etc
Not happy with the way your body looks and feels
Know exactly what you should do to sort that, but struggling to actually do it for various reasons
Turned off by the standard menu of options for addressing that – gyms, slimming clubs, diets, etc

If so, you may be interested in what I do.

Some would call it Personal Training. Some would call it Coaching. I’m not interested in giving what I do labels.

What I am interested in is providing the best possible service (and results) for my clients – whatever that entails.

I work closely with one or two clients at a time to make sure they get exactly what they need.

If you would like to find out more about this, I usually meet for a coffee and a chat. To see if we both think our working together is a good idea.

No squeeze pages, no countdowns, mailing lists or false scarcity.

No plastering this flyer with ‘Before and afters’ – they are ten a penny and my clients don’t want to have pictures of them in their underwear spread around the local area.

Just give me a call and we’ll go from there.

My number is 07914562208.

Ray

Industry/Entity Type

Training

Requirements
Should not have
• Generic before and after or exercise type pictures

```html
<!DOCTYPE html>
<html lang="en">
<head>
<meta charset="utf-8">
<title>Personal Training Flyer</title>
<link rel="stylesheet" href="https://fonts.googleapis.com/css2?family=Oswald:wght@700&family=Raleway:ital,wght@0,400;0,700;1,400&display=swap">
<style>
  :root {
    --page-bg: #e9e6e1;
    --paper: #ffffff;
    --ink: #1a1a1a;
    --panel: #0d0d0d;
    --red: #e21d24;
  }
  * { box-sizing: border-box; margin: 0; padding: 0; }
  html, body { width: 900px; height: 1200px; overflow: hidden; }
  body { background: var(--page-bg); font-family: "Raleway", Arial, sans-serif; color: var(--ink); }

  .flyer {
    position: absolute; left: 82px; top: 77px;
    width: 736px; height: 1046px;
    background: var(--paper);
    overflow: hidden;
    box-shadow: 0 8px 24px rgba(0,0,0,.25);
  }

  .dot-field { position: absolute; border-radius: 50%; }
  .dot-field--right { right: -40px; top: 20px; width: 240px; height: 420px;
    background: radial-gradient(circle, rgba(31,143,214,.35), rgba(124,194,66,.18) 55%, rgba(255,255,255,0) 72%); }
  .dot-field--left { left: -30px; top: 40px; width: 180px; height: 240px;
    background: radial-gradient(circle, rgba(124,194,66,.3), rgba(226,29,36,.15) 55%, rgba(255,255,255,0) 72%); }
  .dot-field--bottom { right: -60px; bottom: -40px; width: 360px; height: 340px;
    background: radial-gradient(circle, rgba(0,0,0,.08), rgba(255,255,255,0) 70%); }

  .swirl { position: absolute; left: 0; top: 0; width: 736px; height: 600px; }

  .hero-photo {
    position: absolute; left: 118px; top: 6px;
    width: 496px; height: 496px; border-radius: 50%;
    background: radial-gradient(circle at 50% 40%, #8a5a3c 0%, #3a2418 28%, #0a0a0a 60%);
    border: 8px solid var(--paper);
  }

  .about-panel {
    position: absolute; left: 13px; top: 240px;
    width: 200px; height: 760px;
    background: var(--panel);
    color: #fff;
    transform: rotate(-5deg);
    transform-origin: top left;
    padding: 26px 12px 0 14px;
    font-size: 15.5px; line-height: 1.3;
    hyphens: auto;
  }
  .about-panel p + p { margin-top: 14px; }
  .about-panel::after {
    content: ""; position: absolute; right: 0; bottom: -22px;
    border-left: 30px solid transparent;
    border-top: 22px solid var(--panel);
  }

  .headline-band {
    position: absolute; left: 250px; top: 470px;
    width: 470px; height: 94px;
    background: var(--red);
    transform: rotate(-7deg);
    transform-origin: left top;
  }
  .headline {
    position: absolute; left: 272px; top: 482px;
    font-family: "Oswald", "Arial Narrow", sans-serif; font-weight: 700;
    font-size: 72px; line-height: 1; letter-spacing: 1px;
    color: #fff; transform: rotate(-7deg); transform-origin: left top;
    white-space: nowrap;
  }

  .checklist {
    position: absolute; left: 276px; top: 604px; width: 420px;
    list-style: none; font-size: 16px; line-height: 1.4;
    transform: rotate(-4deg); transform-origin: left top;
  }
  .checklist li { position: relative; padding-left: 22px; margin-bottom: 3px; }
  .checklist svg { position: absolute; left: 0; top: 3px; width: 17px; height: 17px; }

  .call-to-action { position: absolute; left: 328px; top: 924px; }
  .call-to-action .lead { color: var(--red); font-weight: 700; font-size: 18px; }
  .call-to-action .prompt { font-size: 13.5px; text-transform: uppercase; margin-top: 10px; }
  .contact { display: flex; align-items: center; gap: 10px; margin-top: 10px; margin-left: 26px; }
  .contact svg { width: 34px; height: 34px; }
  .contact .number { color: var(--red); font-weight: 700; font-size: 30px; }
  .contact .dash { color: var(--red); font-weight: 700; font-size: 30px; }
  .contact .name { color: var(--red); font-style: italic; font-size: 30px; }
</style>
</head>
<body>
<svg width="0" height="0" style="position:absolute">
  <symbol id="tick" viewBox="0 0 20 20">
    <circle cx="10" cy="10" r="8.5" fill="none" stroke="#e21d24" stroke-width="2.4"/>
    <path d="M5.5 10.2 L9 13.4 L15.5 6.4" fill="none" stroke="#e21d24" stroke-width="2.6" stroke-linecap="round" stroke-linejoin="round"/>
  </symbol>
</svg>

<main class="flyer">
  <div class="dot-field dot-field--right" role="img" aria-label="Blue and green halftone dot decoration"></div>
  <div class="dot-field dot-field--left" role="img" aria-label="Green and red halftone dot decoration"></div>
  <div class="dot-field dot-field--bottom" role="img" aria-label="Faint grey halftone dot decoration"></div>

  <svg class="swirl" viewBox="0 0 736 600" aria-hidden="true">
    <path d="M90 300 C 60 140, 230 -10, 420 4 C 570 14, 690 120, 700 300"
          fill="none" stroke="#e21d24" stroke-width="34" stroke-linecap="round"/>
  </svg>

  <div class="hero-photo" role="img" aria-label="Photograph of a muscular man posing with arms outstretched against a black background"></div>

  <section class="about-panel">
    <p>Some would call it Personal Training. Some would call it Coaching. I’m not interested in giving what I do labels.</p>
    <p>What I am interested in is providing the best possible service (and results) for my clients – whatever that entails.</p>
    <p>I work closely with one or two clients at a time to make sure they get exactly what they need.</p>
    <p>If you would like to find out more about this, I usually meet for a coffee and a chat. To see if we both think our working together is a good idea.</p>
    <p>No squeeze pages, no countdowns, mailing lists or false scarcity.</p>
    <p>No plastering this flyer with ‘Before and afters’ – they are ten a penny and my clients don’t want to have pictures of them in their underwear spread around the local area.</p>
  </section>

  <div class="headline-band"></div>
  <h1 class="headline">IS THIS YOU:</h1>

  <ul class="checklist">
    <li><svg><use href="#tick"/></svg>Live in East Cheshire</li>
    <li><svg><use href="#tick"/></svg>Male, aged 30-50</li>
    <li><svg><use href="#tick"/></svg>A father</li>
    <li><svg><use href="#tick"/></svg>Cash rich, time poor</li>
    <li><svg><use href="#tick"/></svg>Find handling high pressure at work comfortable</li>
    <li><svg><use href="#tick"/></svg>But have a short fuse out of work – with the wife, kids, life in general, etc</li>
    <li><svg><use href="#tick"/></svg>Not happy with the way your body looks and feels</li>
    <li><svg><use href="#tick"/></svg>Know exactly what you should do to sort that, but struggling to actually do it for various reasons</li>
    <li><svg><use href="#tick"/></svg>Turned off by the standard menu of options for addressing that – gyms, slimming clubs, diets, etc</li>
  </ul>

  <section class="call-to-action">
    <p class="lead">If so, you may be interested in what I do.</p>
    <p class="prompt">Just give me a call and we’ll go from there.</p>
    <div class="contact">
      <svg viewBox="0 0 34 34" aria-hidden="true">
        <circle cx="17" cy="17" r="17" fill="#0d0d0d"/>
        <path d="M12 8.5 l3 4 -2 2.2 c1.2 2.6 3.4 4.8 6 6 l2.2-2 4 3 -1.6 3 c-7.2 0.2 -13.6-6.2 -13.4-13.4z" fill="#fff"/>
      </svg>
      <span class="number">07914562208</span>
      <span class="dash">-</span>
      <span class="name">Ray</span>
    </div>
  </section>
</main>
</body>
</html>
```